Pinecrest Renovations - Get the creative juices going!!

Pinecrest does not do the actual renovation work. The company provides high end project management of renovation (primarily residential - with an eye toward commercial) The renovation work could look very different between projects. This company manages the work of contractors, architects and interior designers (either subcontracted directly by Pinecrest or hired by the client and entrusted to Pinecrest to manage). Clients are high end in the economic scale and the card needs to have a high end feel to it.

The owner is female, but the audience will be heavily slanted male. It should not be a "feminine" or "masculine" looking card. If anything, slant more on the masculine side. Clean, simple, yet creative and artistically appealing. The card design should complement and in no way compete with the logo.

When people think of our company: trust, integrity, dynamic, limitless possibilities, transition, energy, creative. We plan to expand in the future to be international.

There will also be a contest running for stationary. Please check that section, as well.

***Black is 80-90 percent black. Not stark black

Tight timeline. Needs cards printed quickly!

Residential

```html
<!DOCTYPE html>
<html lang="en">
<head>
<meta charset="utf-8">
<title>Pinecrest Renovations – Business Card</title>
<link rel="stylesheet" href="https://fonts.googleapis.com/css2?family=Montserrat:wght@300;400;600&family=Oswald:wght@600&display=swap">
<style>
  :root {
    --teal: #1aa89a;
    --ink: #2d2d2d;
    --paper: #ffffff;
    --map-tone: #e3e5e6;
    --backdrop: #e9e6e1;
  }
  * { box-sizing: border-box; margin: 0; padding: 0; }
  html, body { width: 1200px; height: 970px; overflow: hidden; }
  body {
    background: var(--backdrop);
    font-family: "Montserrat", sans-serif;
    position: relative;
  }
  .card {
    position: absolute;
    left: 210px;
    width: 780px;
    height: 446px;
    background: var(--paper);
    overflow: hidden;
    box-shadow: 0 10px 28px rgba(0,0,0,.18);
  }
  .card--front { top: 26px; }
  .card--back  { top: 498px; }
  .card__bands { position: absolute; inset: 0; width: 100%; height: 100%; }

  .world-map {
    position: absolute;
    left: 150px; top: 20px;
    width: 340px; height: 220px;
    background: radial-gradient(ellipse at center, var(--map-tone) 0%, rgba(227,229,230,.4) 55%, rgba(227,229,230,0) 78%);
  }

  .wordmark {
    position: absolute;
    display: flex;
    align-items: center;
    gap: 12px;
    color: var(--ink);
    font-weight: 600;
    letter-spacing: .04em;
    text-transform: uppercase;
    white-space: nowrap;
  }
  .wordmark__square { width: 30px; height: 30px; background: var(--teal); flex: none; }
  .card--front .wordmark { left: 60px; top: 170px; font-size: 28px; }
  .card--back  .wordmark { left: 50px; top: 200px; font-size: 22px; }
  .card--back  .wordmark__square { width: 26px; height: 26px; }

  .website {
    position: absolute;
    left: 0; right: 0; top: 340px;
    text-align: center;
    color: var(--paper);
    font-size: 20px;
    letter-spacing: .28em;
  }

  .person {
    position: absolute;
    left: 60px; top: 322px;
    color: var(--paper);
  }
  .person__name {
    font-family: "Oswald", sans-serif;
    font-weight: 600;
    font-size: 44px;
    letter-spacing: .04em;
    line-height: 1;
    text-transform: uppercase;
  }
  .person__role {
    margin-top: 8px;
    font-size: 14px;
    letter-spacing: .22em;
    text-transform: uppercase;
  }

  .contacts {
    position: absolute;
    left: 528px; top: 180px;
    list-style: none;
    color: var(--paper);
    font-size: 12px;
    display: grid;
    row-gap: 12px;
  }
  .contacts li { display: flex; align-items: center; gap: 9px; white-space: nowrap; }
  .contacts svg { width: 18px; height: 18px; flex: none; }
</style>
</head>
<body>

<section class="card card--front" aria-label="Card front">
  <svg class="card__bands" viewBox="0 0 780 446" aria-hidden="true">
    <polygon points="0,0 90,0 70,18 0,18" fill="var(--teal)"/>
    <polygon points="660,0 780,0 780,100" fill="var(--teal)"/>
    <polygon points="0,262 370,262 390,282 410,262 780,262 780,446 0,446" fill="var(--teal)"/>
  </svg>
  <div class="wordmark">
    <span class="wordmark__square"></span>
    <span>Pinecrest Renovations</span>
  </div>
  <p class="website">www.pinecrestreno.com</p>
</section>

<section class="card card--back" aria-label="Card back">
  <div class="world-map" role="img" aria-label="Faint world map in light grey behind the wordmark"></div>
  <svg class="card__bands" viewBox="0 0 780 446" aria-hidden="true">
    <polygon points="680,0 780,0 780,446 0,446 0,276 330,276 350,296 370,276 505,276 505,175" fill="var(--teal)"/>
  </svg>
  <div class="wordmark">
    <span class="wordmark__square"></span>
    <span>Pinecrest Renovations</span>
  </div>
  <div class="person">
    <p class="person__name">Daniel Reyes</p>
    <p class="person__role">General Manager</p>
  </div>
  <ul class="contacts">
    <li>
      <svg viewBox="0 0 20 20" aria-hidden="true"><circle cx="10" cy="10" r="9" fill="none" stroke="currentColor" stroke-width="1.4"/><path d="M7 5.5l2 2-1 1.2c.6 1.3 1.5 2.2 2.8 2.8l1.2-1 2 2-1.3 1.5c-3.3-.5-6-3.2-6.5-6.5z" fill="currentColor"/></svg>
      <span>012 555 0147</span>
    </li>
    <li>
      <svg viewBox="0 0 20 20" aria-hidden="true"><circle cx="10" cy="10" r="9" fill="none" stroke="currentColor" stroke-width="1.4"/><rect x="6.5" y="5" width="7" height="10" rx="1" fill="none" stroke="currentColor" stroke-width="1.3"/><line x1="8.5" y1="13" x2="11.5" y2="13" stroke="currentColor" stroke-width="1.1"/></svg>
      <span>012 555 0148</span>
    </li>
    <li>
      <svg viewBox="0 0 20 20" aria-hidden="true"><circle cx="10" cy="10" r="9" fill="none" stroke="currentColor" stroke-width="1.4"/><rect x="5" y="6.5" width="10" height="7" fill="none" stroke="currentColor" stroke-width="1.3"/><path d="M5 6.5l5 4 5-4" fill="none" stroke="currentColor" stroke-width="1.3"/></svg>
      <span>hello@pinecrestreno.com</span>
    </li>
    <li>
      <svg viewBox="0 0 20 20" aria-hidden="true"><circle cx="10" cy="10" r="9" fill="none" stroke="currentColor" stroke-width="1.4"/><circle cx="10" cy="10" r="5" fill="none" stroke="currentColor" stroke-width="1.2"/><line x1="5" y1="10" x2="15" y2="10" stroke="currentColor" stroke-width="1"/><ellipse cx="10" cy="10" rx="2" ry="5" fill="none" stroke="currentColor" stroke-width="1"/></svg>
      <span>www.pinecrestreno.com</span>
    </li>
    <li>
      <svg viewBox="0 0 20 20" aria-hidden="true"><circle cx="10" cy="10" r="9" fill="none" stroke="currentColor" stroke-width="1.4"/><path d="M10 15s-4-4.2-4-6.8a4 4 0 018 0C14 10.8 10 15 10 15z" fill="currentColor"/><circle cx="10" cy="8.2" r="1.4" fill="var(--teal)"/></svg>
      <span>42 Harbor Lane, Suite 3, West</span>
    </li>
  </ul>
</section>

</body>
</html>
```